Menu: A4 (double sided) Lunch/Dinner Menu (one side) + Pizza Menu (other side)

Hello.
We would like to create a new style of menus.
Must be easy to read - a summer feel, crisp, clean, beachy, possible retro feel, colours probably based on our website colours (see address below).
Simple and casual is best as we are a casual beachside Cafe.
This menu will be double sided therefore this job is 2 pages.
If you win this job we will have 2 or 3 more menus for you to create soon after (Drinks, Breakfast, possibly a small Kids menu).
The paper for these menus we expect will be a nice white paper which will then be matte laminated.
Colours possible are the green colour #3a6066, the terracotta on our website logo border and website buttons, maybe a little yellow but must be easy to read on white paper.
Black for text might be okay if this is your best design option.
Please view our website and take a feel for the business, location, the existing website branding and website colours we are trying to achieve, www.saltwrencafe.com.au
We prefer to avoid overwhelming the guest with too many colours on the menus (hence the white paper) as the building is so colourful (La Boca, Argentina, inspired) and the guest experience can be complimented via crisp easy to read menus.
IMPORTANT:
The menus provided please must be fully and easily editable by us in the future.
If you win the job, you must please provide clear instructions on how our staff can edit the menus in the future if project is delivered in Adobe format. Word is also an option for us if you like.
As such, we have attached some documents: the 2x Word documents for the text, 2x .pdf so you can see the fonts and style we were using previously (was printing on recycled brown paper then matte laminated).
If you wished to use the SeaLife Font (this is the existing Font for headings) please let us know as we purchased that font and can provide it.
We have also attached a menu from Quillmont Hotel which we feel has a nice retro feel.
Please include our Instagram in 1 place on the menu @saltwrencafe
Finally, please note,
we never wish to waste anyone's time so we will narrow down the submissions quickly based on first drafts (please know this is because we appreciate your effort and know your time is valuable) and we will then work with the top designer to finalise in a professional fashion.
Thank you.

```html
<!DOCTYPE html>
<html lang="en">
<head>
<meta charset="utf-8">
<title>Salt Wren Cafe – Lunch + Dinner and Pizza Menu</title>
<link href="https://fonts.googleapis.com/css2?family=Nunito:ital,wght@0,800;0,900;1,800&family=Source+Sans+3:ital,wght@0,400;0,600;0,700;1,400;1,600&display=swap" rel="stylesheet">
<style>
:root{
  --bg:#3b3a1f;
  --paper:#ffffff;
  --green:#1fa64a;
  --terracotta:#c9683f;
  --ink:#222222;
  --frame:#cfcfcf;
  --icon:#e3e3e3;
}
*{margin:0;padding:0;box-sizing:border-box}
html,body{width:1200px;height:938px;overflow:hidden;background:var(--bg)}
body{font-family:"Source Sans 3",Arial,sans-serif;color:var(--ink)}
.stage{position:relative;width:1536px;height:1200px;transform:scale(.78125);transform-origin:0 0}
.page{position:absolute;top:14px;width:712px;height:1174px;background:var(--paper)}
.page--lunch{left:44px}
.page--pizza{left:779px;width:711px}
.frame{position:absolute;inset:7px;border:2px dotted var(--frame)}
.icon{position:absolute;background:var(--icon);border-radius:6px}
.block{position:absolute}
.tag{display:inline-block;background:var(--terracotta);color:#fff;font-size:.62em;line-height:1.25;padding:0 3px;margin:0 3px;vertical-align:.15em;font-weight:600}
.rule{position:absolute;height:3px}
.rule--green{background:var(--green)}
.rule--terra{background:var(--terracotta);height:2px}

/* headers */
.title-lunch{position:absolute;right:51px;top:40px;font-family:"Nunito",sans-serif;font-weight:900;font-size:32px;color:var(--green);letter-spacing:.5px}
.legend{position:absolute;right:52px;top:78px;text-align:right;font-size:19px;line-height:24px}
.section-title{position:absolute;left:0;right:0;text-align:center;font-size:25px;color:var(--terracotta);font-weight:400}
.section-title--green{color:var(--green);font-size:26px}

/* rows */
.row{display:flex;align-items:baseline;white-space:nowrap}
.leader{flex:1;border-bottom:2px dotted var(--green);margin:0 8px;transform:translateY(-4px);min-width:10px}
.price{min-width:22px;text-align:right}
.entree{left:52px;width:612px;font-size:16px}
.entree .row{line-height:20.7px}
.item-name{font-weight:700;font-size:20px;text-transform:uppercase;letter-spacing:.2px}
.item-desc{font-size:15px;line-height:21px}
.item .row{line-height:22px;font-size:16px}
.note{font-size:14px;font-style:italic;margin-left:8px;font-weight:400;text-transform:none}
.mains{left:50px;width:614px}
.mains .item .price{font-size:16px}
.platter-name{color:var(--terracotta);font-weight:400;font-size:23px;text-transform:none}
.small{font-size:11px}
.see-over{position:absolute;right:78px;top:1120px;color:var(--terracotta);font-size:17px}

/* pizza page */
.title-pizza{position:absolute;left:49px;top:38px;font-family:"Nunito",sans-serif;font-weight:900;font-size:31px;color:var(--terracotta);letter-spacing:1px}
.subtitle{position:absolute;left:49px;top:76px;font-size:15px}
.band-green{position:absolute;left:51px;top:109px;width:613px;height:23px;background:var(--green);color:#fff;font-size:15px;display:flex;justify-content:center;gap:42px;align-items:center}
.allergy{position:absolute;left:44px;width:623px;top:140px;text-align:center;font-size:13.5px;line-height:17.5px}
.allergy strong{font-weight:700}
.sides{position:absolute;left:0;top:222px;width:711px;height:21px;display:flex;gap:30px}
.sides span{background:var(--terracotta);color:#fff;font-style:italic;font-weight:700;font-size:17px;line-height:21px;text-align:center}
.pizzas{left:46px;width:617px}
.pizzas .item .row{line-height:22.5px}
.pizzas .item-name{font-size:19.5px}
.pizzas .price{font-size:16px;transform:translateY(4px)}
.spicy{font-style:italic;font-size:14px;font-weight:400;text-transform:none;margin-left:6px}
</style>
</head>
<body>
<div class="stage">

  <!-- Lunch + Dinner side -->
  <section class="page page--lunch">
    <div class="frame"></div>
    <div class="icon" role="img" aria-label="Line drawing of drinks glasses and bottles" style="left:56px;top:28px;width:215px;height:116px"></div>
    <h1 class="title-lunch">LUNCH + DINNER</h1>
    <div class="legend">
      <div><span class="tag">v</span>Vegetarian</div>
      <div><span class="tag">gfo</span>Gluten Friendly Optional</div>
      <div>please ask</div>
    </div>
    <div class="rule rule--green" style="left:51px;top:156px;width:613px"></div>

    <h2 class="section-title" style="top:170px">ENTREE <span class="icon" role="img" aria-label="Plate icon" style="position:relative;display:inline-block;width:48px;height:24px;vertical-align:middle;left:auto;top:auto"></span></h2>
    <div class="block entree" style="top:202px">
      <div class="row"><span>Garlic Bread (2)<span class="tag">v</span></span><span class="leader"></span><span class="price">8</span></div>
      <div class="row"><span>Salt &amp; Pepper Squid&nbsp; w/ thai dipping sauce</span><span class="leader"></span><span class="price">18</span></div>
      <div class="row"><span>Duo of Dip<span class="tag">v</span>w/ pita</span><span class="leader"></span><span class="price">14</span></div>
      <div class="row"><span>Bowl of Chips<span class="tag">v</span>w/ tomato sauce</span><span class="leader"></span><span class="price">11</span></div>
      <div class="row"><span>Seasoned Wedges<span class="tag">v</span>w/ sour cream &amp; sweet chilli</span><span class="leader"></span><span class="price">15</span></div>
      <div class="row"><span>Onion Rings (12)<span class="tag">v</span>beer battered w/ tangy mayo</span><span class="leader"></span><span class="price">13</span></div>
      <div class="row"><span>Vietnamese Spring Rolls (3)&nbsp; chicken, home-made</span><span class="leader"></span><span class="price">11</span></div>
      <div class="row"><span>Bruschetta (1)<span class="tag">v</span>w/ olive oil, tomato &amp; red onion salsa, balsamic glaze, feta</span><span class="leader"></span><span class="price">10</span></div>
    </div>
    <div class="rule rule--green" style="left:51px;top:379px;width:613px;height:2px"></div>

    <h2 class="section-title" style="top:387px"><span class="icon" role="img" aria-label="Chef hat icon" style="position:relative;display:inline-block;width:30px;height:30px;vertical-align:middle;left:auto;top:auto;margin-right:10px"></span>MAINS</h2>
    <div class="block mains" style="top:415px">
      <div class="item"><div class="row"><span class="item-name">The Fish &amp; Chips</span><span class="leader"></span><span class="price">25</span></div><div class="item-desc">house-crumbed butterfish w/ chips, tartare &amp; side salad</div></div>
      <div class="item"><div class="row"><span class="item-name">Smokey Beef &amp; Bacon Cheese Burger</span><span class="leader"></span><span class="price">23</span></div><div class="item-desc">w/ chips, onion rings, gerkins &amp; tangy mayo</div><div class="item-desc" style="padding-left:34px">+ jalapenos 2 &nbsp;&nbsp;&nbsp;&nbsp; + pineapple 2</div></div>
      <div class="item"><div class="row"><span class="item-name">Salt &amp; Pepper Squid</span><span class="leader"></span><span class="price">31</span></div><div class="item-desc">golden tangles w/ chips, thai dipping sauce &amp; side salad</div></div>
      <div class="item"><div class="row"><span class="item-name">Seafood Basket</span><span class="leader"></span><span class="price">31</span></div><div class="item-desc">crumbed butterfish, grilled prawns, salt &amp; pepper squid, chips, tartare &amp; side salad</div></div>
      <div class="item"><div class="row"><span class="item-name">Atlantic Salmon</span><span class="leader"></span><span class="price">31</span></div><div class="item-desc">served w/ mash, teriyaki sauce &amp; winter vegetables &nbsp;&nbsp;&nbsp;&nbsp;&nbsp; <span style="font-size:13px">(contains breadcrumbs)</span></div></div>
      <div class="item"><div class="row"><span class="item-name">Chicken Parmigiana</span><span class="leader"></span><span class="price">27</span></div><div class="item-desc">house-crumbed breast schnitzel, napoli sauce, mozzarella, chips &amp; side salad</div><div class="item-desc" style="padding-left:96px">+ bacon and pineapple 4 &nbsp;&nbsp;&nbsp;&nbsp; + jalapenos and pineapple 4</div></div>
    </div>
    <div class="rule rule--terra" style="left:51px;top:718px;width:613px;height:3px"></div>

    <div class="block mains" style="top:743px">
      <div class="item"><div class="row"><span class="item-name platter-name"><span class="icon" role="img" aria-label="Serving cloche icon" style="position:relative;display:inline-block;width:62px;height:26px;vertical-align:middle;left:auto;top:auto;margin-right:10px"></span>SALT WREN PLATTER for 2</span><span class="leader"></span><span class="price">90</span></div><div class="item-desc">beer battered flathead, salt &amp; pepper squid, prawn skewers, grilled chicken, lamb &amp; chorizo,</div><div class="item-desc">served with antipasto, dipping sauces, pita &amp; garlic bread &nbsp;&nbsp;&nbsp;&nbsp; (+45 pp)</div></div>
      <div class="item"><div class="row"><span class="item-name">New York Sirloin<span class="tag">gfo</span></span><span class="leader"></span><span class="price">38</span></div><div class="item-desc">400g MSA w/ mash &amp; winter vegetables</div><div class="item-desc">choose: mushroom gravy or classic gravy &nbsp;&nbsp;&nbsp;&nbsp;&nbsp;&nbsp;&nbsp;&nbsp; or &nbsp;&nbsp;&nbsp;&nbsp;&nbsp;&nbsp;&nbsp;&nbsp;&nbsp;&nbsp;&nbsp;&nbsp;&nbsp; surf 'n' turf<span class="tag">gfo</span>+6</div><div class="item-desc small">(Please allow 35+ minutes for "well-done")</div></div>
      <div class="item"><div class="row"><span class="item-name">Chicken Caesar</span><span class="leader"></span><span class="price">27</span></div><div class="item-desc">w/ bacon, anchovies, egg, caesar dressing, parmesan, spanish onion, garlic bread</div></div>
      <div class="item"><div class="row"><span class="item-name">Lamb Salad<span class="tag">gfo</span></span><span class="leader"></span><span class="price">30</span></div><div class="item-desc">skewers w/ traditional greek salad, tzatziki &amp; garlic bread + extra lamb 8</div></div>
      <div class="item"><div class="row"><span class="item-name">Thai Chicken Curry<span class="note">spicy/mild</span><span class="tag">gfo</span></span><span class="leader"></span><span class="price">26</span></div><div class="item-desc">traditional recipe, w/ jasmine rice &amp; papadums</div></div>
      <div class="item"><div class="row"><span class="item-name">Beach Burger<span class="tag">v</span></span><span class="leader"></span><span class="price">23</span></div><div class="item-desc">house-made pea &amp; corn ricotta fritter, pineapple, w/ wedges, onion rings, sweet chilli</div></div>
      <div class="item"><div class="row"><span class="item-name">Vegan Curry<span class="note">spicy/mild</span><span class="tag">gfo</span><span class="tag">v</span></span><span class="leader"></span><span class="price">24</span></div><div class="item-desc">chickpea &amp; pumpkin w/ fresh tomatoes &amp; basil, jasmine rice &amp; papadums</div></div>
    </div>
    <div class="see-over">please see over for</div>
    <div class="icon" role="img" aria-label="Pizza icon" style="left:640px;top:1114px;width:38px;height:38px;border-radius:50%"></div>
  </section>

  <!-- Pizza side -->
  <section class="page page--pizza">
    <div class="frame"></div>
    <h1 class="title-pizza">PIZZA</h1>
    <div class="subtitle">ALL 12" with house-made tomato base &amp; mozzarella</div>
    <div class="icon" role="img" aria-label="Pizza line icon" style="left:560px;top:28px;width:76px;height:72px;border-radius:50%"></div>
    <div class="band-green"><span>v&nbsp; Vegetarian</span><span>Gluten Free base +$4</span><span>Vegan Cheese +$3</span></div>
    <p class="allergy"><strong>Allergies? Please let us know!</strong> All care is taken to cater for allergies including gluten, however our kitchen is small and we do not have separate preparation or cooking areas. As such, there is risk of cross-contact with your allergen and we are unable to guarantee allergen-free meals. Olives may very rarely contain pips.</p>
    <div class="sides"><span style="width:224px">garlic bread&nbsp; 8</span><span style="width:204px">greek salad&nbsp; 16</span><span style="width:223px">garden salad&nbsp; 12</span></div>

    <h2 class="section-title section-title--green" style="top:257px">STANDARD PIZZA</h2>
    <div class="block pizzas" style="top:283px">
      <div class="item"><div class="row"><span class="item-name">Hawaiian</span><span class="leader"></span><span class="price">22</span></div><div class="item-desc">ham, pineapple</div></div>
      <div class="item"><div class="row"><span class="item-name">Margherita<span class="tag">v</span></span><span class="leader"></span><span class="price">22</span></div><div class="item-desc">marinated &amp; diced tomatoes, fresh basil</div></div>
      <div class="item"><div class="row"><span class="item-name">BBQ Chicken</span><span class="leader"></span><span class="price">26</span></div><div class="item-desc">chicken, salami, tomato, spanish onion, bbq sauce</div></div>
      <div class="item"><div class="row"><span class="item-name">Chorizo<span class="spicy">spicy</span></span><span class="leader"></span><span class="price">26</span></div><div class="item-desc">chorizo, salami, tomato, mushrooms, spanish onion</div></div>
      <div class="item"><div class="row"><span class="item-name">Salt Wren Special</span><span class="leader"></span><span class="price">26</span></div><div class="item-desc">ham, salami, prawns, kalamata olives, roasted capsicum, mushrooms, spanish onion</div></div>
      <div class="item"><div class="row"><span class="item-name">Meat Lovers</span><span class="leader"></span><span class="price">26</span></div><div class="item-desc">chicken, bacon, salami, ham, bbq sauce</div></div>
      <div class="item"><div class="row"><span class="item-name">Mona Lisa</span><span class="leader"></span><span class="price">26</span></div><div class="item-desc">chicken, pineapple, ham, spanish onion, mushrooms</div></div>
      <div class="item"><div class="row"><span class="item-name">Puttanesca</span><span class="leader"></span><span class="price">26</span></div><div class="item-desc">anchovies, capers, salami, kalamata olives, roasted capsicum, parmesan</div></div>
      <div class="item"><div class="row"><span class="item-name">Tropical Chicken<span class="spicy">spicy</span></span><span class="leader"></span><span class="price">26</span></div><div class="item-desc">chicken, pineapple, spanish onion, chilli, tomato, mushrooms</div></div>
      <div class="item"><div class="row"><span class="item-name">Vegetarian<span class="tag">v</span></span><span class="leader"></span><span class="price">26</span></div><div class="item-desc">roasted capsicum, tomato, mushrooms, artichokes, kalamata olives, spanish onion</div></div>
      <div class="item"><div class="row"><span class="item-name">Build Your Own<span class="tag">v</span></span><span class="leader"></span><span class="price">26</span></div><div class="item-desc">tomato base, mozzarella &amp; four toppings</div></div>
    </div>
    <div class="rule rule--terra" style="left:49px;top:768px;width:614px"></div>

    <h2 class="section-title section-title--green" style="top:775px">GOURMET PIZZA</h2>
    <div class="block pizzas" style="top:808px;left:51px;width:612px">
      <div class="item"><div class="row"><span class="item-name">Caveman</span><span class="leader"></span><span class="price">29</span></div><div class="item-desc">chicken, lamb, pork sausage, chorizo, salami, bacon, spanish onion, caramelised onion,<br>smokey bbq sauce</div></div>
      <div class="item"><div class="row"><span class="item-name">Spicy Prawn &amp; Basil Pesto<span class="spicy">spicy</span></span><span class="leader"></span><span class="price">29</span></div><div class="item-desc">prawns, roasted capsicum, chilli, spring onion, basil pesto</div></div>
      <div class="item"><div class="row"><span class="item-name">Gourmet Vegetarian<span class="tag">v</span></span><span class="leader"></span><span class="price">29</span></div><div class="item-desc">pumpkin, eggplant, semi-dried tomatoes, roasted capsicum, red onion, bulgarian feta,<br>kalamata olives, spinach</div></div>
      <div class="item"><div class="row"><span class="item-name">Desert Rider<span class="spicy">spicy</span></span><span class="leader"></span><span class="price">29</span></div><div class="item-desc">chilli jam, jalapeno peppers, mushrooms, bacon, chilli, chorizo, spanish onion</div></div>
      <div class="item"><div class="row"><span class="item-name">Lamb Pizza</span><span class="leader"></span><span class="price">29</span></div><div class="item-desc">lamb, red onion, fresh tomato, tzatziki, spring onion</div></div>
      <div class="item"><div class="row"><span class="item-name">Los Pollos</span><span class="leader"></span><span class="price">29</span></div><div class="item-desc">chicken, pumpkin, basil pesto, spinach, feta, pine nuts</div></div>
      <div class="item"><div class="row"><span class="item-name">Seafood Pizza</span><span class="leader"></span><span class="price">29</span></div><div class="item-desc">array of seafood</div></div>
    </div>
  </section>

</div>
</body>
</html>
```